Chinese Artwork Gallery and Tea House need website design

This is a challenging website design, as the styles combines contemporary layout infused with oriental artwork style. Our company run a oriental gallery/tea house from Sydney, specialising selling oriental antique replicate such as terra-cotta warriors, porcelain vases, bronze cups, traditional Chinese painting and calligraphy, tea and tea sets. The colour scheme will incorporate the existing gold, red and black being used for our logo.

Please include in the homepage a section with large sliding image to showcase individual antique pieces, as well as image to link to 6 categories of products we are selling in retail store and online store which are Porcelain, Bronze, Terra Cotta, Painting and Calligraphy, Chinese Artwork, Tea & Tea Sets. The home page needs to highlight our brand and the design pattern we have included in the logo design. Colour wise, red, black, gold and white. I hope above helps.

```html
<!DOCTYPE html>
<html lang="en">
<head>
<meta charset="utf-8">
<title>About Lanshui</title>
<link href="https://fonts.googleapis.com/css2?family=Oswald:wght@300;500&family=Cormorant+Garamond:wght@300&family=Noto+Serif+TC:wght@300&display=swap" rel="stylesheet">
<style>
  :root {
    --red: #b50d0d;
    --deep-red: #7d0808;
    --black: #111111;
    --ink: #2a2a2a;
    --paper: #e4e4e4;
    --gold: #d8a92a;
  }
  html, body {
    margin: 0;
    padding: 0;
    width: 1200px;
    height: 820px;
    overflow: hidden;
    background: var(--paper);
  }
  .page {
    position: relative;
    width: 1200px;
    height: 820px;
    background: var(--paper);
    font-family: "Oswald", sans-serif;
  }
  .sidebar {
    position: absolute;
    left: 0;
    top: 0;
    width: 76px;
    height: 820px;
    background: var(--red);
    text-align: center;
  }
  .menu-icon {
    position: absolute;
    left: 28px;
    top: 34px;
  }
  .brand-mark {
    position: absolute;
    left: 0;
    top: 92px;
    width: 76px;
    text-align: center;
  }
  .brand-mark .square {
    display: block;
    width: 22px;
    height: 22px;
    margin: 0 auto 8px;
    background: var(--black);
  }
  .brand-mark .name {
    font-family: "Oswald", sans-serif;
    font-weight: 300;
    font-size: 13px;
    color: var(--black);
    letter-spacing: 0.5px;
  }
  .vertical-name {
    position: absolute;
    left: 0;
    top: 214px;
    width: 76px;
    margin: 0;
    padding: 0;
    list-style: none;
  }
  .vertical-name li {
    font-family: "Cormorant Garamond", serif;
    font-weight: 300;
    font-size: 36px;
    line-height: 68.6px;
    color: var(--deep-red);
  }
  .chinese-name {
    position: absolute;
    left: 0;
    top: 720px;
    width: 76px;
    font-family: "Noto Serif TC", serif;
    font-weight: 300;
    font-size: 26px;
    color: var(--deep-red);
    letter-spacing: 1px;
  }
  .hero {
    position: absolute;
    left: 76px;
    top: 0;
    width: 1124px;
    height: 330px;
    background:
      linear-gradient(to bottom, rgba(228,228,228,0) 0%, rgba(228,228,228,0) 45%, rgba(228,228,228,1) 100%),
      linear-gradient(100deg, #5a1c1c 0%, #6b6b6b 25%, #2a2a2a 45%, #8a3030 62%, #3a3030 72%, #8e7f6e 85%, #b0968a 100%);
  }
  .title {
    position: absolute;
    left: 331px;
    top: 80px;
    margin: 0;
    font-weight: 500;
    font-size: 78px;
    line-height: 1;
  }
  .title .lead {
    display: block;
    color: var(--deep-red);
  }
  .title .main {
    display: block;
    margin-left: 141px;
    margin-top: -4px;
    color: var(--black);
  }
  .quote-mark {
    position: absolute;
    left: 330px;
    top: 364px;
  }
  .about-text {
    position: absolute;
    left: 401px;
    top: 360px;
    width: 660px;
    margin: 0;
    font-weight: 300;
    font-size: 19px;
    line-height: 28px;
    color: var(--ink);
  }
  .about-text p { margin: 0; }
</style>
</head>
<body>
<div class="page">
  <nav class="sidebar">
    <svg class="menu-icon" width="22" height="18" viewBox="0 0 22 18" aria-label="Menu">
      <rect x="0" y="1" width="22" height="3" fill="var(--gold)"/>
      <rect x="0" y="7.5" width="22" height="3" fill="var(--gold)"/>
      <rect x="0" y="14" width="22" height="3" fill="var(--gold)"/>
    </svg>
    <div class="brand-mark">
      <span class="square"></span>
      <span class="name">Lanshui</span>
    </div>
    <ul class="vertical-name">
      <li>L</li><li>A</li><li>N</li><li>S</li><li>H</li><li>U</li><li>I</li>
    </ul>
    <div class="chinese-name">蘭水</div>
  </nav>

  <div class="hero" role="img" aria-label="Tea house interior with dark wooden seating, red cushions and a carved stone tea disc"></div>

  <h1 class="title">
    <span class="lead">About</span>
    <span class="main">Lanshui</span>
  </h1>

  <svg class="quote-mark" width="52" height="68" viewBox="0 0 52 68" aria-hidden="true">
    <path d="M2 68 V26 Q2 4 22 0 V12 Q14 16 14 26 H22 V68 Z" fill="var(--black)"/>
    <path d="M30 68 V26 Q30 4 50 0 V12 Q42 16 42 26 H50 V68 Z" fill="var(--black)"/>
  </svg>

  <div class="about-text">
    <p>Lan meaning orchid, is the symbolic flower from the mythical orient. Shui has a literal meaning of water, connotating prosperity and luxury in traditional Chinese culture.</p>
    <p>At Lanshui, we present you the authentic oriental cultural experience through a rich collection of traditional Chinese artwork and artifact with premium quality and finishing.</p>
    <p>At Lanshui, we handpick the highest grade tea from China to bring you to the amorous and tranquil world of Chinese tea garden.</p>
    <p>At Lanshui, we await you.</p>
  </div>
</div>
</body>
</html>
```